New, modern business card for growing audiology practice

We need a new business card for our audiology practice. Our logo and website have recently changed (more modern) and we want our business cards to reflect this change.
We conduct hearing tests, perform earwax removals, and fit & dispense hearing aids to our patients. We are a family owned practice in which the owner is the one who works directly with the patient. I have attached logos in various formats to use, as well as two ideas I found on this website; as well as a scanned copy of our current logo. Good luck!

Industry/Entity Type

Business

Contact Information for Business Card

Company name: Birchmont Hearing Center
Provider name: Peter Lowsby, Au.D. F/NSO
Phone number: (555) 318-6042
Address: 287 W. Hollister Rd. Alder Falls, OH 40000
email: birchmonthearing@quillpost.net
website: birchmonthearing.net

Colors
000000
aaaaaa
dbdbdb
cacaca
9bcb3c
afd23c
cadf82
b1b1b1

Requirements
Must have
• My card must include information in the "details" section. In the attached images, I found a few that I liked and I would like to model after - "steady strivin'" and "Sound Lab Clinic".
• Must be horizontal.
• Must include logos provided. I uploaded them in various file formats and various ways.
• Must match logo font, if possible, if not, please get as close as you can.
Nice to have
• I really like the idea of having a color on one side with just the logo and company name and the contact information and provider name on the other side. I also really like the idea of having the main color dominating on the logo/company side with accent of that same color on the contact side of the card.
Should not have
• Must not be vertical.

```html
<!DOCTYPE html>
<html lang="en">
<head>
<meta charset="utf-8">
<title>Birchmont Hearing Center – Business Card</title>
<link rel="stylesheet" href="https://fonts.googleapis.com/css2?family=Questrial&display=swap">
<style>
  :root {
    --bg: #3a3a3a;
    --card: #f2f2f2;
    --green: #6a9f3a;
    --lime: #9bcb3c;
    --ink: #3b3b3b;
    --muted: #4a4a4a;
  }
  * { margin: 0; padding: 0; box-sizing: border-box; }
  html, body { width: 1200px; height: 834px; overflow: hidden; }
  body {
    background: var(--bg);
    font-family: "Questrial", "Century Gothic", sans-serif;
    display: flex;
    flex-direction: column;
    align-items: center;
    justify-content: center;
    gap: 30px;
  }
  .card {
    position: relative;
    width: 640px;
    height: 366px;
    background: linear-gradient(135deg, #ffffff 0%, var(--card) 100%);
    box-shadow: 0 6px 18px rgba(0,0,0,.35);
  }
  .brand {
    position: absolute;
    display: flex;
    align-items: center;
    gap: 16px;
  }
  .brand-dot {
    width: 46px; height: 46px;
    border-radius: 50%;
    background: var(--green);
  }
  .brand-name {
    color: var(--ink);
    font-size: 22px;
    line-height: 1.05;
    text-transform: uppercase;
    letter-spacing: .5px;
  }
  .card-front .brand { left: 92px; top: 168px; }
  .web-band {
    position: absolute;
    left: 400px; right: 0; top: 104px;
    height: 38px;
    background: var(--green);
    color: #fff;
    font-size: 13px;
    display: flex;
    align-items: center;
    padding-left: 22px;
  }
  .card-back .brand { left: 104px; top: 180px; }
  .card-back .brand-dot { background: var(--lime); }
  .details {
    position: absolute;
    left: 330px; top: 116px;
    color: var(--muted);
    font-size: 12px;
  }
  .provider {
    color: var(--lime);
    font-size: 16px;
    font-weight: 700;
    text-transform: uppercase;
    letter-spacing: .4px;
    margin-bottom: 12px;
  }
  .address { line-height: 1.5; margin: 0 0 12px 14px; }
  .contact-list { list-style: none; margin-left: 14px; }
  .contact-list li {
    display: flex; align-items: center; gap: 10px;
    line-height: 1.6;
  }
  .contact-list svg { width: 12px; height: 12px; flex: none; }
</style>
</head>
<body>
  <section class="card card-front">
    <div class="brand">
      <span class="brand-dot"></span>
      <div class="brand-name">Birchmont<br>Hearing<br>Center</div>
    </div>
    <div class="web-band">www.birchmonthearing.net</div>
  </section>

  <section class="card card-back">
    <div class="brand">
      <span class="brand-dot"></span>
      <div class="brand-name">Birchmont<br>Hearing<br>Center</div>
    </div>
    <div class="details">
      <p class="provider">Peter Lowsby, Au.D. F/NSO</p>
      <p class="address">287 W. Hollister<br>Rd. Alder Falls, OH 40000</p>
      <ul class="contact-list">
        <li>
          <svg viewBox="0 0 12 12" fill="none" stroke="#9bcb3c" stroke-width="1.3"><path d="M1 4c0-2 10-2 10 0v1H8V4H4v1H1z"/><rect x="2.5" y="6" width="7" height="5" rx="1"/></svg>
          (555) 318-6042
        </li>
        <li>
          <svg viewBox="0 0 12 12" fill="none" stroke="#9bcb3c" stroke-width="1.3"><rect x="1" y="2.5" width="10" height="7"/><path d="M1 2.5l5 4 5-4"/></svg>
          birchmonthearing@quillpost.net
        </li>
        <li>
          <svg viewBox="0 0 12 12" fill="none" stroke="#9bcb3c" stroke-width="1.3"><circle cx="6" cy="6" r="5"/><path d="M1 6h10M6 1c2.5 3 2.5 7 0 10M6 1c-2.5 3-2.5 7 0 10"/></svg>
          www.birchmonthearing.net
        </li>
      </ul>
    </div>
  </section>
</body>
</html>
```